TallonCryo Website - Biologics storage and handling

I would like a beginning design on a website for TallonCryo:

A Boston-based company dedicated to sourcing, storing, and supplying biologic materials of all kinds to the life sciences and scientific markets. From starting reagents, to basic and intermediate materials, to final synthesized and engineered products, we provide value throughout the biologics supply chain. TallonCryo provides backup, overflow, emergency, and stocking storage solutions to companies on a temporary or permanent basis. Life sciences companies can take advantage of the fact that the company is located in the middle of the Boston/Cambridge biotechnology corridor in order to have quick and efficient access to their cold chain materials. Out of state companies can leverage TallonCryo’s location for efficient distribution of materials to partner and client organizations. We also provide other value added services to organizations that do not have the local manpower, such as sourcing, supply, and distribution of materials.

The design should be mostly a white background with clean, linear, geometric colors added in according to the blue and orange color scheme represented in the corporate logo attached.

The website needs to communicate reliable service and provide the concept of a company dedicated to handling and providing client biological samples in a secure and efficient manner.

Some local competitors are:
1. Orlen BioServices: www.orlenbio-example.com
2. VaultiCore: www.vaulticore-example.com

From a design perspective, I like the Meridel Thera website:

www.merideltheraexample.com

Target Market(s)

Life sciences companies and other organizations

Industry/Entity Type

Biotechnology

Coding

Coded - Design and coding required

Number of Pages Required

5+ page

Font styles to use
Sans Serif

Colors
3176b5
0455a3
f37122

Requirements
Must have
• Tabs for pages:
About - Company information.
Platform - Inventory and sample management cloud platform; temperature profiling, logging, and reporting.
Services - Refrigeration and freezing services for biological samples, logistics services, sourcing services, courier services.
Updates - News, events, blog.
Login portal - Entry point for getting into platform. Maybe some freemium content here.
Nice to have
• Please be creative about website page sections, vibrant colors according to my established color scheme, and clean, linear, geometric shapes. I would like a white background with nice colors, clean lines and borders, and a very contemporary look. I want o
Should not have
• This is not a Business to Consumer business. This is a Business to Business enterprise. There should not be consumer oriented language. It is more about service and relationship management.

```html
<!DOCTYPE html>
<html lang="en">
<head>
<meta charset="utf-8">
<title>TallonCryo — Biologics sourcing, storage and supply</title>
<link rel="stylesheet" href="https://fonts.googleapis.com/css2?family=Nunito:wght@300;400;600;700;800&family=Montserrat:wght@500;600&display=swap">
<style>
:root{
  --blue-deep:#0455a3;
  --blue:#3176b5;
  --navy:#174a92;
  --navy-dark:#0f1d45;
  --orange:#f37122;
  --ink:#1e2b4f;
  --muted:#6b7283;
  --white:#ffffff;
  --body:"Nunito",sans-serif;
  --label:"Montserrat",sans-serif;
}
*{box-sizing:border-box;margin:0;padding:0}
html,body{width:1200px;height:3044px;overflow:hidden}
body{position:relative;background:var(--white);font-family:var(--body);color:var(--ink)}
.abs{position:absolute}

/* header */
.site-header{left:0;top:0;width:1200px;height:63px;background:var(--white)}
.brand{left:215px;top:18px;display:flex;align-items:center;gap:8px;font-family:var(--body);font-weight:600;font-size:19px;color:var(--blue-deep)}
.brand-square{width:14px;height:14px;background:var(--orange)}
.main-nav{top:26px;font-family:var(--label);font-size:9.5px;font-weight:500;color:var(--ink);letter-spacing:.3px}
.login{left:898px;top:24px;display:flex;align-items:center;gap:5px;font-family:var(--label);font-size:9.5px;font-weight:600;color:var(--blue-deep)}

/* hero */
.hero{left:0;top:63px;width:1200px;height:481px;background:linear-gradient(120deg,#1a4e88 0%,#1f5a98 40%,#0f3f73 100%)}
.hero-title{left:215px;top:201px;font-size:38px;line-height:39.5px;font-weight:300;color:var(--white)}
.hero-title strong{font-weight:700}
.hero-arrow{left:215px;top:384px}

/* intro */
.intro{left:215px;top:589px;width:510px;font-size:23.5px;line-height:29px;font-weight:300;color:var(--ink)}
.intro strong{font-weight:700}
.text-link{font-family:var(--label);font-size:9px;font-weight:600;letter-spacing:2px;color:var(--blue-deep)}

/* activities */
.section-title{width:1200px;left:0;text-align:center;font-size:31px;font-weight:300;color:var(--ink)}
.section-title strong{font-weight:700}
.section-sub{width:1200px;left:0;text-align:center;font-size:9.5px;line-height:15px;color:var(--muted)}
.activity{width:244px;height:244px;border-radius:50%;display:flex;flex-direction:column;align-items:center;justify-content:center;text-align:center}
.activity-light{background:radial-gradient(circle,#fff 78%,#eef6fb 100%);border:1.5px solid var(--blue-deep)}
.activity-light h3{font-size:24px;font-weight:700;color:var(--blue-deep)}
.activity-dark{background:var(--navy);color:var(--white)}
.activity-dark h3{font-size:24px;font-weight:600}
.activity-dark p{font-size:10.5px;line-height:14px;margin-top:8px;width:190px}

/* platform band */
.platform{left:0;top:1301px;width:1200px;height:351px;background:linear-gradient(135deg,#2a7bd0 0%,#1c64b8 45%,#2f7fcf 75%,#1a5aa8 100%)}
.platform-title{left:213px;top:1413px;font-size:31px;line-height:32px;font-weight:300;color:var(--white)}
.platform-title strong{font-weight:700}
.btn{display:flex;align-items:center;justify-content:center;gap:6px;border:1.5px solid var(--white);border-radius:20px;font-family:var(--label);font-size:9px;font-weight:600;letter-spacing:1.8px;color:var(--white)}

/* services band */
.services{left:0;top:1652px;width:1200px;height:444px;background:var(--orange)}
.services-title{left:213px;top:1694px;font-size:31px;line-height:31px;font-weight:300;color:var(--white)}
.services-title strong{font-weight:700}
.service{width:180px;color:var(--white)}
.service h4{margin-top:16px;font-size:16.5px;line-height:19px;font-weight:600}
.service p{margin-top:13px;font-size:9.5px;line-height:15px}

/* news */
.news-card{width:247px}
.news-media{width:247px;height:149px;border-radius:4px}
.news-card h5{margin:22px 5px 0;font-size:13.5px;line-height:18px;font-weight:700;color:var(--blue-deep)}
.news-card time{display:block;margin:10px 5px 0;font-size:9.5px;color:var(--muted)}
.news-card p{margin:16px 5px 0;font-size:9.5px;line-height:15px;color:var(--muted)}

/* contact */
.contact-band{left:0;top:2599px;width:1200px;height:369px;background:linear-gradient(160deg,#172456 0%,#0f1d45 60%,#0c173a 100%)}
.contact-box{left:230px;top:2708px;width:772px;height:151px;background:var(--navy)}
.contact-text{left:277px;top:2754px;font-size:25.5px;line-height:32px;font-weight:300;color:var(--white)}
.contact-text strong{font-weight:700}

/* footer */
.site-footer{left:0;top:2968px;width:1200px;height:76px}
.legal{left:215px;top:2999px;font-size:9px;color:var(--ink)}
.legal a{color:var(--blue-deep);text-decoration:underline}
.follow{left:852px;top:2994px;display:flex;align-items:center;gap:12px;font-size:9px;color:var(--ink)}
.dot{width:11px;height:11px;border-radius:50%;background:var(--blue-deep)}
</style>
</head>
<body>

<header class="abs site-header">
  <div class="abs brand"><span class="brand-square"></span>TallonCryo</div>
  <nav>
    <span class="abs main-nav" style="left:556px">ABOUT</span>
    <span class="abs main-nav" style="left:608px">PLATFORM</span>
    <span class="abs main-nav" style="left:678px">SERVICES</span>
    <span class="abs main-nav" style="left:743px">UPDATES</span>
    <span class="abs main-nav" style="left:806px">CONTACT</span>
  </nav>
  <div class="abs login">
    <svg width="13" height="13" viewBox="0 0 13 13" fill="none" stroke="#f37122" stroke-width="1.1"><circle cx="6.5" cy="6.5" r="5.8"/><circle cx="6.5" cy="5.2" r="2"/><path d="M2.8 10.6c1-1.6 2.2-2.3 3.7-2.3s2.7.7 3.7 2.3"/></svg>
    LOGIN PORTAL
  </div>
</header>

<section class="abs hero" role="img" aria-label="Laboratory technician handling frozen sample racks, tinted deep blue"></section>
<h1 class="abs hero-title">We are dedicated to<br>sourcing, storing, and<br>supplying <strong>biologic</strong><br><strong>materials</strong></h1>
<svg class="abs hero-arrow" width="10" height="70" viewBox="0 0 10 70" fill="none" stroke="#fff" stroke-width="1.2"><path d="M5 0v68M1 63l4 5 4-5"/></svg>

<p class="abs intro"><strong>TallonCryo</strong> is dedicated to sourcing, storing, and supplying biologic materials of all kinds to the life sciences and scientific markets. From starting reagents, to basic and intermediate materials, to final synthesized and engineered products, we provide value throughout the biologics supply chain.</p>
<span class="abs text-link" style="left:218px;top:811px">ABOUT US &rarr;</span>

<h2 class="abs section-title" style="top:880px">Explore our <strong>activities</strong></h2>
<p class="abs section-sub" style="top:926px">We provide backup, overflow, emergency, and stocking storage solutions to companies<br>on a temporary or permanent basis.</p>

<div class="abs activity activity-light" style="left:218px;top:998px"><h3>Source</h3></div>
<div class="abs activity activity-dark" style="left:477px;top:998px"><h3>Store</h3><p>GxP storage of biologics materials at various temperatures</p></div>
<div class="abs activity activity-light" style="left:738px;top:998px"><h3>Supply</h3></div>

<section class="abs platform" role="img" aria-label="Blue geometric faceted background"></section>
<h2 class="abs platform-title"><strong>Inventory and sample</strong><br><strong>management</strong> cloud platform</h2>
<div class="abs btn" style="left:215px;top:1499px;width:203px;height:37px">DISCOVER THE PLATFORM &rarr;</div>

<section class="abs services"></section>
<h2 class="abs services-title"><strong>Biological storage</strong><br>facilities and services</h2>
<div class="abs btn" style="left:810px;top:1711px;width:173px;height:37px">VIEW ALL SERVICES &rarr;</div>

<div class="abs service" style="left:217px;top:1828px">
  <svg width="58" height="58" viewBox="0 0 58 58" fill="none" stroke="#fff" stroke-width="2.2" stroke-linecap="round"><path d="M6 52C20 40 24 30 30 20s14-14 22-14"/><path d="M6 38c8 0 14 4 18 10M20 8c2 8 8 14 18 16"/><path d="M14 44l6-6M22 34l8-6M32 22l6-8"/></svg>
  <h4>Biological<br>storage</h4>
  <p>Lorem ipsum dolor sit amet, con-<br>sectetur adipiscing elit, sed do<br>eiusmod tempor incididunt ut<br>labore et dolore magna aliqua.<br>Quis ipsum suspendisse.</p>
</div>
<div class="abs service" style="left:424px;top:1828px">
  <svg width="58" height="58" viewBox="0 0 58 58" fill="none" stroke="#fff" stroke-width="2.2" stroke-linejoin="round"><path d="M29 6l22 10v26L29 52 7 42V16z"/><path d="M7 16l22 10 22-10M29 26v26"/></svg>
  <h4>logistics<br>services</h4>
  <p>Lorem ipsum dolor sit amet, con-<br>sectetur adipiscing elit, sed do<br>eiusmod tempor incididunt ut<br>labore et dolore magna aliqua.<br>Quis ipsum suspendisse.</p>
</div>
<div class="abs service" style="left:629px;top:1828px">
  <svg width="58" height="58" viewBox="0 0 58 58" fill="none" stroke="#fff" stroke-width="2.2" stroke-linecap="round" stroke-linejoin="round"><path d="M24 6l10 6-10 18-10-6z"/><path d="M30 24c10 2 14 10 10 18"/><circle cx="20" cy="40" r="6"/><path d="M10 52h36M26 46l8 6"/></svg>
  <h4>Sourcing<br>services</h4>
  <p>Lorem ipsum dolor sit amet, con-<br>sectetur adipiscing elit, sed do<br>eiusmod tempor incididunt ut<br>labore et dolore magna aliqua.<br>Quis ipsum suspendisse.</p>
</div>
<div class="abs service" style="left:831px;top:1828px">
  <svg width="64" height="58" viewBox="0 0 64 58" fill="none" stroke="#fff" stroke-width="2.2" stroke-linejoin="round"><path d="M10 12h32v30H10zM42 22h10l8 10v10H42"/><circle cx="20" cy="44" r="5" fill="#f37122"/><circle cx="50" cy="44" r="5" fill="#f37122"/><path d="M2 20h12M4 28h12M2 36h10"/></svg>
  <h4>Courier<br>services</h4>
  <p>Lorem ipsum dolor sit amet, con-<br>sectetur adipiscing elit, sed do<br>eiusmod tempor incididunt ut<br>labore et dolore magna aliqua.<br>Quis ipsum suspendisse.</p>
</div>

<h2 class="abs section-title" style="top:2150px"><strong>News</strong> and updates</h2>
<p class="abs section-sub" style="top:2196px">Lorem ipsum dolor sit amet, consectetur adipiscing elit tempor incididunt<br>ut labore et dolore</p>

<article class="abs news-card" style="left:215px;top:2261px">
  <div class="news-media" role="img" aria-label="Gloved hands handling sample vials in a cold room" style="background:linear-gradient(135deg,#8e949c,#5d6670)"></div>
  <h5>Lorem ipsum dolor sit amet, consect etur adipiscing elit,</h5>
  <time>April 24, 2020</time>
  <p>Lorem ipsum dolor sit amet, consectetur adipiscing elit tempor incididunt ut labore et dolore magna aliqua.</p>
</article>
<article class="abs news-card" style="left:475px;top:2261px">
  <div class="news-media" role="img" aria-label="Hand pulling a frosted rack from a freezer" style="background:linear-gradient(135deg,#d4d8dc,#9aa2aa)"></div>
  <h5>Sed do eiusmod tempor incididunt ut labore et dolore</h5>
  <time>April 24, 2020</time>
  <p>Lorem ipsum dolor sit amet, consectetur adipiscing elit tempor incididunt ut labore et dolore magna aliqua.</p>
</article>
<article class="abs news-card" style="left:736px;top:2261px">
  <div class="news-media" role="img" aria-label="Laboratory staff in white coats working at a bench" style="background:linear-gradient(135deg,#e6e8ea,#b9c0c6)"></div>
  <h5>Quis ipsum suspendisse ultrices gravida. Risus commo</h5>
  <time>April 24, 2020</time>
  <p>Lorem ipsum dolor sit amet, consectetur adipisc-ing elit tempor incididunt ut labore et dolore magna aliqua.</p>
</article>

<section class="abs contact-band" role="img" aria-label="Dark navy textured background"></section>
<div class="abs contact-box"></div>
<p class="abs contact-text">We’re friendly and available<br>to assist. <strong>Reach out to us anytime</strong></p>
<div class="abs btn" style="left:779px;top:2768px;width:142px;height:37px">CONTACT US &rarr;</div>

<footer class="abs site-footer"></footer>
<p class="abs legal">© 2020 All Rights Reserved. <a>Privacy Policy</a> &nbsp;|&nbsp; <a>Terms &amp; Conditions</a></p>
<div class="abs follow">Follow Us on <span class="dot"></span><span class="dot"></span><span class="dot"></span></div>

</body>
</html>
```